Business Card Design Project

double sided, embossed, name & logo on front font sonsie one, back Name Marisol Venkamp, mobile 0468201934, Phone 73519086,
email marisol@brightspanservices.com, use sysbols on the back for example an envelope for email, a telephone for phone number etc.symbol slate grey writing navy blue

Industry/Entity Type

Business

```html
<!DOCTYPE html>
<html lang="en">
<head>
<meta charset="utf-8">
<title>Brightspan Services – Business Card</title>
<link rel="stylesheet" href="https://fonts.googleapis.com/css2?family=Sonsie+One&family=Tinos&display=swap">
<style>
  :root {
    --navy: #012d8c;
    --slate: #4a4d52;
    --white: #ffffff;
    --rule: #8f9fd8;
    --label: #111111;
  }
  * { margin: 0; padding: 0; box-sizing: border-box; }
  html, body { width: 1200px; height: 382px; overflow: hidden; background: var(--white); }
  .sheet { position: relative; width: 1200px; height: 382px; font-family: "Tinos", "Times New Roman", serif; }

  /* Front side */
  .front-header-mark {
    position: absolute; right: 620px; top: 38px;
    font-family: "Sonsie One", cursive; font-size: 15px; color: var(--navy); white-space: nowrap;
  }
  .front-panel {
    position: absolute; left: 0; top: 72px; width: 600px; height: 260px;
    background: var(--navy); overflow: hidden;
  }
  .front-name {
    position: absolute; left: 0; right: 0; top: 84px; text-align: center;
    font-family: "Sonsie One", cursive; font-size: 27px; color: var(--white); white-space: nowrap;
  }

  /* Back side */
  .back-band {
    position: absolute; left: 600px; top: 15px; width: 600px; height: 55px; background: var(--navy);
  }
  .back-name {
    position: absolute; left: 0; right: 0; top: 3px; text-align: center;
    font-size: 40px; line-height: 48px; color: var(--white);
  }
  .contact-list { position: absolute; left: 726px; top: 162px; list-style: none; }
  .contact-item {
    display: flex; align-items: center; gap: 8px; height: 37.5px;
    font-size: 28px; color: var(--slate);
  }
  .contact-item svg { flex: none; }
  .back-rule { position: absolute; left: 600px; top: 331px; width: 600px; height: 1px; background: var(--rule); }

  /* Print labels */
  .side-label { position: absolute; top: 355px; font-size: 18px; color: var(--label); }
  .side-label.front { left: 213px; }
  .side-label.back { left: 834px; }
  .label-leader { position: absolute; left: 300px; top: 370px; width: 490px; border-top: 1px dotted #9a9a9a; }
</style>
</head>
<body>
<main class="sheet">
  <div class="front-header-mark">Brightspan Services</div>
  <section class="front-panel">
    <div class="front-name">Brightspan Services</div>
  </section>

  <section class="back-band">
    <div class="back-name">Marisol Venkamp</div>
  </section>

  <ul class="contact-list">
    <li class="contact-item">
      <svg width="18" height="28" viewBox="0 0 18 28" aria-label="Mobile">
        <rect x="4" y="0" width="2" height="4" fill="var(--slate)"/>
        <rect x="1" y="3" width="16" height="24" rx="2" fill="var(--slate)"/>
        <rect x="4" y="6" width="10" height="7" fill="#fff"/>
        <g fill="#fff"><rect x="4" y="16" width="2.5" height="2"/><rect x="7.8" y="16" width="2.5" height="2"/><rect x="11.5" y="16" width="2.5" height="2"/>
        <rect x="4" y="20" width="2.5" height="2"/><rect x="7.8" y="20" width="2.5" height="2"/><rect x="11.5" y="20" width="2.5" height="2"/></g>
      </svg>
      <span>0468201934</span>
    </li>
    <li class="contact-item">
      <svg width="18" height="28" viewBox="0 0 18 28" aria-label="Phone">
        <rect x="4" y="0" width="2" height="4" fill="var(--slate)"/>
        <rect x="1" y="3" width="16" height="24" rx="2" fill="var(--slate)"/>
        <rect x="4" y="6" width="10" height="7" fill="#fff"/>
        <g fill="#fff"><rect x="4" y="16" width="2.5" height="2"/><rect x="7.8" y="16" width="2.5" height="2"/><rect x="11.5" y="16" width="2.5" height="2"/>
        <rect x="4" y="20" width="2.5" height="2"/><rect x="7.8" y="20" width="2.5" height="2"/><rect x="11.5" y="20" width="2.5" height="2"/></g>
      </svg>
      <span>73519086</span>
    </li>
    <li class="contact-item">
      <svg width="32" height="26" viewBox="0 0 32 26" aria-label="Email" style="margin-left:-8px">
        <path d="M2 11 L16 2 L30 11 V24 H2 Z" fill="#fff" stroke="var(--slate)" stroke-width="2.2" stroke-linejoin="round"/>
        <rect x="8" y="7" width="16" height="9" fill="var(--slate)"/>
        <path d="M2 11 L16 20 L30 11" fill="none" stroke="var(--slate)" stroke-width="2.2"/>
        <path d="M2 24 L13 17 M30 24 L19 17" stroke="var(--slate)" stroke-width="2"/>
      </svg>
      <span>marisol@brightspanservices.com</span>
    </li>
  </ul>
  <div class="back-rule"></div>

  <span class="side-label front">FRONT</span>
  <div class="label-leader"></div>
  <span class="side-label back">BACK</span>
</main>
</body>
</html>
```